I need a Label design for my copper 71 kombucha brand that is launching soon

I want a label to go on my copper 71 kombucha bottle.
I have a logo image uploaded in the files but I am open to changes to this logo or even a completely New one if you think you can do better. This logo is based on the idea of an s-shaped naga. I particularly like the nagas from temples in luang prabang.
I also want to include the slogan - dare to be delicious.
The label should be some kind of oval at 80mm high by 70mm wide.
The label will go on a clear glass bottle. The kombucha will be visible and comes in different shades of red,yellow and purple.
The word kombucha should be clearly visible.
i want a very colorful, playful label. I'm very keen to see your ideas and I want something original.
Fermented foods and beverages

```html
<!DOCTYPE html>
<html lang="en">
<head>
<meta charset="utf-8">
<title>copper 71 Kombucha Label</title>
<link rel="stylesheet" href="https://fonts.googleapis.com/css2?family=Oswald:wght@600&family=Montserrat:wght@500;600&display=swap">
<style>
  :root {
    --magenta: #c2166f;
    --charcoal: #3a3a3b;
    --white: #ffffff;
    --ink-grey: #4a4a4a;
    --leaf-light: #8cc152;
    --leaf-dark: #3f7a25;
  }
  html, body {
    margin: 0;
    padding: 0;
    width: 1047px;
    height: 1200px;
    overflow: hidden;
    background: var(--white);
  }
  .label {
    display: block;
    width: 1047px;
    height: 1200px;
  }
  .brand-name {
    font-family: "Montserrat", sans-serif;
    font-weight: 500;
    fill: var(--ink-grey);
  }
  .product-title {
    font-family: "Oswald", sans-serif;
    font-weight: 600;
    fill: var(--white);
  }
  .slogan, .volume {
    font-family: "Montserrat", sans-serif;
    font-weight: 600;
    fill: var(--white);
  }
</style>
</head>
<body>
<svg class="label" viewBox="0 0 792 908" xmlns="http://www.w3.org/2000/svg">
  <defs>
    <clipPath id="label-shape">
      <ellipse cx="396" cy="454" rx="396" ry="454"/>
    </clipPath>
    <radialGradient id="leaf-tone" cx="50%" cy="40%" r="60%">
      <stop offset="0%" stop-color="#8cc152"/>
      <stop offset="100%" stop-color="#3f7a25"/>
    </radialGradient>
  </defs>

  <g class="label-body" clip-path="url(#label-shape)">
    <rect class="label-ground" x="0" y="0" width="792" height="908" fill="var(--white)"/>
    <path class="wave-panel" fill="var(--magenta)"
      d="M0,168 C120,128 230,132 300,210 C350,268 380,300 420,300 C470,300 500,250 540,200 C600,130 690,118 792,160 L792,908 L0,908 Z"/>
    <path class="wave-edge" fill="none" stroke="var(--charcoal)" stroke-width="18"
      d="M0,168 C120,128 230,132 300,210 C350,268 380,300 420,300 C470,300 500,250 540,200 C600,130 690,118 792,160"/>
    <rect class="tea-band" x="0" y="657" width="792" height="48" fill="var(--charcoal)"/>
  </g>

  <g class="brand-mark">
    <circle cx="262" cy="112" r="14" fill="var(--magenta)"/>
    <text class="brand-name" x="288" y="126" font-size="40">copper 71</text>
  </g>

  <text class="product-title" x="400" y="470" text-anchor="middle" font-size="148"
    textLength="612" lengthAdjust="spacingAndGlyphs">KOMBUCHA</text>
  <text class="slogan" x="396" y="527" text-anchor="middle" font-size="33"
    textLength="492" lengthAdjust="spacingAndGlyphs">DARE TO BE DELICIOUS</text>

  <g class="tea-medallion">
    <circle cx="396" cy="690" r="124" fill="var(--white)" stroke="var(--charcoal)" stroke-width="18"/>
    <ellipse role="img" aria-label="Fresh green tea leaves on a stem"
      cx="396" cy="675" rx="105" ry="130" fill="url(#leaf-tone)"/>
  </g>

  <text class="volume" x="396" y="866" text-anchor="middle" font-size="25">100ML</text>
</svg>
</body>
</html>
```